Australian Software Consultancy needs new Business Card Design

Design Business Card based on existing design artefacts (attached). We are open to all designs. As its a 2 sided design and we thought it might be quite striking to have one side with a black background and te other side with a white background.

Target Market(s)

Financial Services mainly.

Industry/Entity Type

Business

Contact Information for Business Card

Requirements
Must have
• Funky design using our existing assets

```html
<!DOCTYPE html>
<html lang="en">
<head>
<meta charset="utf-8">
<title>Northvale Business Card</title>
<link rel="stylesheet" href="https://fonts.googleapis.com/css2?family=Montserrat:wght@600;700&family=Open+Sans:wght@400;600;700&display=swap">
<style>
  :root {
    --page-bg: #e9e7e5;
    --card-black: #1d1d1f;
    --card-black-deep: #161617;
    --emboss: #2c2c2e;
    --emboss-edge: #3a3a3c;
    --text-white: #ffffff;
    --text-soft: #e4e4e4;
    --accent-red: #e3262b;
  }
  * { box-sizing: border-box; margin: 0; padding: 0; }
  html, body { width: 1200px; height: 715px; overflow: hidden; }
  body {
    background: var(--page-bg);
    font-family: "Open Sans", Arial, sans-serif;
    position: relative;
  }
  .card {
    position: absolute;
    top: 203px;
    width: 540px;
    height: 309px;
    background: linear-gradient(160deg, var(--card-black) 0%, var(--card-black-deep) 100%);
    overflow: hidden;
    box-shadow: 0 6px 18px rgba(0,0,0,0.18);
  }
  .card--front { left: 40px; }
  .card--back  { left: 620px; }

  /* Front side */
  .front-mark {
    position: absolute;
    inset: 0;
    display: flex;
    align-items: center;
    justify-content: center;
    gap: 16px;
  }
  .front-mark__circle {
    width: 86px; height: 86px;
    border-radius: 50%;
    border: 7px solid var(--emboss-edge);
  }
  .front-mark__name {
    font-family: "Montserrat", Arial, sans-serif;
    font-weight: 700;
    font-size: 34px;
    letter-spacing: 1px;
    color: var(--emboss-edge);
  }

  /* Back side */
  .brand-name {
    position: absolute;
    left: 36px; top: 38px;
    font-family: "Montserrat", Arial, sans-serif;
    font-weight: 700;
    font-size: 31px;
    letter-spacing: 0.5px;
    color: var(--text-white);
  }
  .person {
    position: absolute;
    left: 36px; top: 132px;
    color: var(--text-white);
  }
  .person__name { font-weight: 700; font-size: 17px; line-height: 1.2; }
  .person__role { font-size: 11px; color: var(--text-soft); margin-top: 2px; }
  .contact-list {
    position: absolute;
    left: 36px; top: 180px;
    list-style: none;
  }
  .contact-list__item {
    display: flex;
    align-items: center;
    gap: 10px;
    font-size: 12.5px;
    color: var(--text-soft);
    height: 19px;
  }
  .contact-list__icon { width: 10px; height: 10px; fill: var(--accent-red); flex: none; }
  .mark-circle {
    position: absolute;
    right: 100px; top: 126px;
    width: 44px; height: 44px;
    border-radius: 50%;
    border: 3px solid var(--accent-red);
  }
  .mark-bar {
    position: absolute;
    right: 0; top: 136px;
    width: 98px; height: 24px;
    background: var(--text-white);
  }
  .red-band {
    position: absolute;
    left: 0; right: 0; bottom: 0;
    height: 12px;
    background: var(--accent-red);
  }
</style>
</head>
<body>
  <section class="card card--front" aria-label="Card front">
    <div class="front-mark">
      <span class="front-mark__circle"></span>
      <span class="front-mark__name">NORTHVALE</span>
    </div>
  </section>

  <section class="card card--back" aria-label="Card back">
    <div class="brand-name">NORTHVALE</div>
    <div class="person">
      <div class="person__name">Daniel Reeve</div>
      <div class="person__role">Managing Director</div>
    </div>
    <ul class="contact-list">
      <li class="contact-list__item">
        <svg class="contact-list__icon" viewBox="0 0 10 10"><path d="M2 0h2l1 2.5-1.3 1a6 6 0 0 0 2.8 2.8l1-1.3L10 6v2a2 2 0 0 1-2 2A8 8 0 0 1 0 2a2 2 0 0 1 2-2z"/></svg>
        1300 482 915
      </li>
      <li class="contact-list__item">
        <svg class="contact-list__icon" viewBox="0 0 10 10"><path d="M5 0a5 5 0 1 0 0 10A5 5 0 0 0 5 0zm0 1.2c.6.7 1 1.9 1.1 3.2H3.9C4 3.1 4.4 1.9 5 1.2zM1.3 5.6h1.4c.1 1.1.4 2.1.8 2.8A3.8 3.8 0 0 1 1.3 5.6zm0-1.2a3.8 3.8 0 0 1 2.2-2.8c-.4.7-.7 1.7-.8 2.8zM5 8.8c-.6-.7-1-1.9-1.1-3.2h2.2C6 6.9 5.6 8.1 5 8.8zm1.5-.4c.4-.7.7-1.7.8-2.8h1.4a3.8 3.8 0 0 1-2.2 2.8zm.8-4c-.1-1.1-.4-2.1-.8-2.8a3.8 3.8 0 0 1 2.2 2.8z"/></svg>
        www.northvaleadvisory.com
      </li>
      <li class="contact-list__item">
        <svg class="contact-list__icon" viewBox="0 0 10 10"><path d="M0 2h10v6H0zm1 .8v.3l4 2.6 4-2.6v-.3z"/></svg>
        daniel.reeve@northvale.com
      </li>
    </ul>
    <span class="mark-circle"></span>
    <span class="mark-bar"></span>
    <div class="red-band"></div>
  </section>
</body>
</html>
```